Norwegian language blog www.lumadio.com / www.lumadio.no

I want to make a blog where I share my thoughts and ideas about Norwegian language. I already have a YouTube channel with almost 40000 followers and a podcast with more than 10000 listeners, so this blog will be the extention of those channels. In addition I have my own online school, check www.vilpa.noI have a logo and everything, so I just need a fresh vibrant blog to go with my concept. I want to keep the colors in my logo and also add my logo of course. Then the blog should be easy to read. I need some pictures of the Norwegian flag or something.I want a fun and cool design.
Check my youtube here: https://www.videohub.example/channel/UCxqWPT415mKaZ8Lf2dHoRwn?view_as=subscriber
Website here: www.vilpa.no

The blog will be for my new domain www.lumadio.no and I also have the same domain with www.lumadio.com - I want to put them both in one URL, like when you write www.lumadio.no or .com you will reach the same page.

Target Market(s)

Student who want to learn Norwegian and learn about Norwegian culture

Industry/Entity Type

Education

Coding

Coded - Design and coding required

Number of Pages Required

1 page

Font styles to use
Sans Serif

Colors
e34398
00a990
f78f20
0492cd
86cfc6
85cae6
f8ba93
eda3c7
ffc214

Requirements
Must have
• The colors of my logo, check www.vilpa.no
• Cool and elegant layout
• Pictures of Norway
• Picture of me
• Picture of the Norwegian flag
Should not have
• too many colors and pictures of random people

```html
<!DOCTYPE html>
<html lang="en">
<head>
<meta charset="utf-8">
<title>Lumadio – Norwegian language blog</title>
<link href="https://fonts.googleapis.com/css2?family=Poppins:wght@300;400;500;600&display=swap" rel="stylesheet">
<style>
:root{
  --pink:#e34398;
  --teal:#00a990;
  --orange:#f78f20;
  --blue:#0492cd;
  --mint:#86cfc6;
  --sky:#85cae6;
  --yellow:#ffc214;
  --ink:#333333;
  --soft:#f4f4f4;
  --dark:#353535;
  --white:#ffffff;
}
*{box-sizing:border-box;margin:0;padding:0}
html,body{width:1200px;height:2724px;overflow:hidden}
body{position:relative;font-family:'Poppins',sans-serif;color:var(--ink);background:var(--white)}
.abs{position:absolute}
.top-strip{left:0;top:0;width:1200px;height:3px;background:linear-gradient(90deg,var(--blue) 0 25%,var(--pink) 25% 44%,var(--orange) 44% 62%,var(--teal) 62% 81%,var(--pink) 81%)}
.site-header{left:0;top:3px;width:1200px;height:88px;background:var(--white);box-shadow:0 2px 6px rgba(0,0,0,.08);z-index:3}
.brand{left:92px;top:24px;display:flex;align-items:center;gap:14px}
.brand-dot{width:38px;height:38px;border-radius:50%;background:var(--teal)}
.brand-name{font-size:32px;font-weight:300;color:var(--ink)}
.main-nav a{position:absolute;top:39px;font-size:12px;color:var(--ink);text-decoration:none;white-space:nowrap}
.social{top:32px;width:26px;height:26px;border-radius:50%;border:1px solid #ddd;background:var(--white)}
.social.is-active{background:#e62117;border-color:#e62117}
.hero-greet{left:92px;top:186px;font-size:33px;font-weight:300}
.hero-name{left:92px;top:226px;font-size:45px;font-weight:300;color:var(--teal);white-space:nowrap}
.hero-name span{font-size:33px;color:var(--ink)}
.hero-text{left:93px;top:300px;width:510px;font-size:16.5px;line-height:31px}
.signature{left:100px;top:480px;width:125px;height:62px;background:linear-gradient(90deg,#ddd,#bbb);opacity:.5;border-radius:4px}
.btn{display:flex;align-items:center;justify-content:center;background:var(--pink);color:var(--white);border-radius:26px;font-size:16px;text-transform:uppercase}
.hero-btn{left:84px;top:580px;width:158px;height:50px}
.hero-art{left:600px;top:91px;width:600px;height:560px;z-index:1}
.band-soft{left:0;width:1200px;background:var(--soft)}
.section-title{font-size:28px;font-weight:300;display:flex;align-items:center;gap:16px;white-space:nowrap}
.section-title::after{content:"";width:35px;height:2px;background:var(--orange)}
.more-link{left:1028px;top:752px;font-size:13px;color:var(--pink);text-decoration:underline}
.card{width:314px;background:var(--white);box-shadow:0 2px 8px rgba(0,0,0,.07)}
.card-media{position:absolute;left:0;top:0;width:100%}
.card-title{position:absolute;left:30px;font-size:22px;font-weight:300;line-height:28px}
.play{position:absolute;width:54px;height:54px}
.course-title{left:89px;top:1763px;font-size:34px;font-weight:300;line-height:38px}
.course-rule{left:90px;top:1875px;width:123px;height:3px;background:var(--orange)}
.course-text{left:84px;top:1919px;width:570px;font-size:22px;font-weight:300;line-height:33.5px;color:#555}
.course-btn{left:85px;top:2111px;width:193px;height:50px}
.portrait{left:680px;top:1758px;width:540px;height:540px;border-radius:50%;background:var(--sky);overflow:hidden;z-index:2;box-shadow:0 30px 40px rgba(180,140,0,.25)}
.portrait-photo{position:absolute;left:60px;top:60px;width:420px;height:480px;border-radius:48% 48% 0 0;background:linear-gradient(180deg,#d8d8d8,#8a8a8a 60%,#3a3a3a)}
.newsletter{left:0;top:2248px;width:1200px;height:192px;background:var(--yellow)}
.news-title{left:88px;top:2273px;font-size:26px;font-weight:300;color:var(--white);text-transform:uppercase}
.news-input{left:84px;top:2332px;width:400px;height:50px;border-radius:25px 0 0 25px;background:var(--white);font-size:13px;color:#777;padding:16px 28px}
.news-btn{left:422px;top:2332px;width:184px;height:50px;border-radius:25px;background:var(--teal);color:var(--white);font-size:12px;font-weight:600;display:flex;align-items:center;justify-content:center}
.site-footer{left:0;top:2440px;width:1200px;height:284px;background:var(--dark)}
.footer-mark{left:592px;top:2488px;width:48px;height:48px;border-radius:50%;background:var(--teal)}
.footer-nav a{position:absolute;top:2564px;font-size:13px;color:#ccc;text-decoration:none}
.copyright{left:0;top:2587px;width:1200px;text-align:center;font-size:12px;color:#bbb}
</style>
</head>
<body>
<div class="abs top-strip"></div>
<header class="abs site-header">
  <div class="abs brand" style="top:21px"><span class="brand-dot"></span><span class="brand-name">Lumadio</span></div>
  <nav class="main-nav">
    <a style="left:444px">HOME</a><a style="left:539px">ABOUT ME</a><a style="left:634px">MY BLOG</a><a style="left:729px">SERVICES</a><a style="left:824px">CONTACTUS</a>
  </nav>
  <span class="abs social" style="left:963px"></span>
  <span class="abs social" style="left:1001px"></span>
  <span class="abs social" style="left:1039px"></span>
  <span class="abs social is-active" style="left:1077px"></span>
</header>

<section class="hero">
  <div class="abs hero-greet">Hello,</div>
  <h1 class="abs hero-name" style="font-weight:300">Sunniva Aasland <span>here..</span></h1>
  <p class="abs hero-text">Lorem Ipsum is simply dummy text of the printing and typesetting industry. Lorem Ipsum has been the industry's standard dummy text ever since the 1500s, when an unknown printer took a galley of type and scrambled it to make a type specimen book.</p>
  <div class="abs signature" role="img" aria-label="Handwritten signature"></div>
  <div class="abs btn hero-btn">Know more</div>
  <svg class="abs hero-art" viewBox="0 0 600 560">
    <defs><linearGradient id="photoTone" x1="0" y1="0" x2="0" y2="1"><stop offset="0" stop-color="#e8c9a8"/><stop offset=".6" stop-color="#c9a070"/><stop offset="1" stop-color="#3b3330"/></linearGradient></defs>
    <path d="M130 0 H600 V350 C540 420 470 500 380 530 C240 560 60 480 22 310 C0 200 50 80 130 0 Z" fill="var(--mint)"/>
    <path d="M130 60 C170 20 300 0 380 30 C450 60 480 160 470 300 C465 400 440 480 380 530 C260 560 80 480 50 330 C35 220 80 110 130 60 Z" fill="url(#photoTone)" role="img" aria-label="Portrait photo of the blogger"/>
    <circle cx="447" cy="471" r="67" fill="var(--white)"/>
    <circle cx="447" cy="471" r="62" fill="#ef4045" role="img" aria-label="Norwegian flag"/>
  </svg>
</section>

<section class="abs band-soft" style="top:693px;height:566px"></section>
<h2 class="abs section-title" style="left:82px;top:735px">Latest videos</h2>
<a class="abs more-link">more videos</a>

<article class="abs card" style="left:84px;top:811px;height:331px">
  <div class="card-media" style="height:182px;background:linear-gradient(135deg,#7d8a86,#c9b7a8)" role="img" aria-label="Video thumbnail: winter walk by a stream"></div>
  <svg class="play" style="left:242px;top:155px" viewBox="0 0 54 54"><circle cx="27" cy="27" r="27" fill="var(--pink)"/><circle cx="27" cy="27" r="15" fill="none" stroke="#fff" stroke-width="3"/><path d="M23 20 L34 27 L23 34 Z" fill="#fff"/></svg>
  <h3 class="card-title" style="top:207px;font-weight:300">Video 482<br>Adventskalender 5.<br>desember</h3>
</article>
<article class="abs card" style="left:436px;top:811px;height:331px">
  <div class="card-media" style="height:182px;background:linear-gradient(135deg,#b89a8a,#3a3550)" role="img" aria-label="Video thumbnail: blogger speaking to camera"></div>
  <svg class="play" style="left:242px;top:155px" viewBox="0 0 54 54"><circle cx="27" cy="27" r="27" fill="var(--pink)"/><circle cx="27" cy="27" r="15" fill="none" stroke="#fff" stroke-width="3"/><path d="M23 20 L34 27 L23 34 Z" fill="#fff"/></svg>
  <h3 class="card-title" style="top:207px;font-weight:300">Video 481<br>Adventskalender 4.<br>desember</h3>
</article>
<article class="abs card" style="left:794px;top:811px;height:331px">
  <div class="card-media" style="height:182px;background:linear-gradient(135deg,#2b3040,#c9ab88)" role="img" aria-label="Video thumbnail: winter evening outdoors"></div>
  <svg class="play" style="left:242px;top:155px" viewBox="0 0 54 54"><circle cx="27" cy="27" r="27" fill="var(--pink)"/><circle cx="27" cy="27" r="15" fill="none" stroke="#fff" stroke-width="3"/><path d="M23 20 L34 27 L23 34 Z" fill="#fff"/></svg>
  <h3 class="card-title" style="top:207px;font-weight:300">Video 482<br>Adventskalender 5.<br>desember</h3>
</article>

<h2 class="abs section-title" style="left:83px;top:1291px">Latest Poscats</h2>

<article class="abs card" style="left:84px;top:1368px;height:246px">
  <div class="card-media" style="height:107px;background:#f3f3f3"><div class="abs" style="left:30px;top:12px;width:256px;height:80px;background:linear-gradient(180deg,transparent 10%,var(--blue) 35% 65%,transparent 90%)" role="img" aria-label="Audio waveform"></div></div>
  <svg class="play" style="left:244px;top:80px" viewBox="0 0 54 54"><circle cx="27" cy="27" r="27" fill="var(--pink)"/><circle cx="27" cy="27" r="15" fill="none" stroke="#fff" stroke-width="3"/><path d="M23 20 L34 27 L23 34 Z" fill="#fff"/></svg>
  <h3 class="card-title" style="top:138px;font-weight:300">Podcast<br>Title</h3>
</article>
<article class="abs card" style="left:436px;top:1368px;height:246px">
  <div class="card-media" style="height:107px;background:#f3f3f3"><div class="abs" style="left:30px;top:12px;width:256px;height:80px;background:linear-gradient(180deg,transparent 10%,var(--blue) 35% 65%,transparent 90%)" role="img" aria-label="Audio waveform"></div></div>
  <svg class="play" style="left:242px;top:80px" viewBox="0 0 54 54"><circle cx="27" cy="27" r="27" fill="var(--pink)"/><circle cx="27" cy="27" r="15" fill="none" stroke="#fff" stroke-width="3"/><path d="M23 20 L34 27 L23 34 Z" fill="#fff"/></svg>
  <h3 class="card-title" style="top:138px;font-weight:300">Podcast<br>Title</h3>
</article>
<article class="abs card" style="left:800px;top:1368px;height:246px">
  <div class="card-media" style="height:107px;background:#f3f3f3"><div class="abs" style="left:30px;top:12px;width:256px;height:80px;background:linear-gradient(180deg,transparent 10%,var(--blue) 35% 65%,transparent 90%)" role="img" aria-label="Audio waveform"></div></div>
  <svg class="play" style="left:243px;top:80px" viewBox="0 0 54 54"><circle cx="27" cy="27" r="27" fill="var(--pink)"/><circle cx="27" cy="27" r="15" fill="none" stroke="#fff" stroke-width="3"/><path d="M23 20 L34 27 L23 34 Z" fill="#fff"/></svg>
  <h3 class="card-title" style="top:138px;font-weight:300">Podcast<br>Title</h3>
</article>

<section class="abs band-soft" style="top:1681px;height:567px"></section>
<h2 class="abs course-title">Study Norwegian courses<br>where you want, when you want!</h2>
<div class="abs course-rule"></div>
<p class="abs course-text">If you want to learn Norwegian from a professional. If you are an expat and looking to have accredited and approved hours of language course and social studies course for permanent residency purpose.</p>
<div class="abs btn course-btn">Book a course</div>

<section class="abs newsletter"></section>
<h2 class="abs news-title" style="font-weight:300">Subscribe for my newsletter</h2>
<div class="abs news-input">Enter your email address</div>
<div class="abs news-btn">SUBSCRIBE</div>

<div class="abs portrait"><div class="portrait-photo" role="img" aria-label="Black and white portrait of the teacher"></div></div>

<footer class="abs site-footer"></footer>
<div class="abs footer-mark"></div>
<nav class="footer-nav">
  <a style="left:394px">Home</a><a style="left:489px">About me</a><a style="left:584px">My blog</a><a style="left:679px">Services</a><a style="left:774px">Contactus</a>
</nav>
<p class="abs copyright">© lumadio - 2018 | All rights reserved</p>
</body>
</html>
```